App landing page and Quill Nook template

I am building a web-based app to help people manage their lives. The app divides their life into 4 categories, Self, Relationships, Career, and Finance. I need a landing page for this application which will feature as a dashboard for each of the categories. The page will be dynamically updated as updates are received from the app. The logo will be a key feature of the page. There will be a menu to the left-hand side. A banner at the top will include interactive icons for the user to navigate the site, manage their account and logout.
I also need a template page for users to present the Quills Nook to the end users where users can store passwords, important documents, and other important information. This template will present Secrets in either a list format or in an itemized box format.
I have attached the Application Logo for reference.

```html
<!DOCTYPE html>
<html lang="en">
<head>
<meta charset="utf-8">
<title>PathHaven – Home</title>
<link href="https://fonts.googleapis.com/css2?family=Poppins:wght@400;500;600;700;800&display=swap" rel="stylesheet">
<style>
  :root{
    --navy:#10325a;
    --blue:#0e5fa6;
    --rule:#2a7fd0;
    --red:#e8254f;
    --yellow:#f6c20f;
    --green:#1aa523;
    --ink:#161616;
    --muted:#2b2b2b;
    --white:#ffffff;
    --black:#000000;
  }
  *{box-sizing:border-box;margin:0;padding:0}
  html,body{width:923px;height:1200px;overflow:hidden;background:var(--white);font-family:"Poppins",sans-serif;color:var(--ink)}
  .page{position:relative;width:923px;height:1200px}

  .sidebar{position:absolute;left:5px;top:4px;width:185px;height:544px;background:var(--navy);border-radius:14px;color:var(--white)}
  .sidebar-brand{position:absolute;left:0;right:0;top:28px;display:flex;align-items:center;justify-content:center;gap:6px;font-weight:700;font-size:15px}
  .sidebar-brand .dot{width:12px;height:12px;border-radius:50%;background:var(--white)}
  .nav-global{position:absolute;left:14px;top:105px;display:flex;align-items:center;gap:8px;font-size:14px}
  .nav-section{position:absolute;left:2px;right:2px;display:flex;align-items:center;font-size:12.5px}
  .nav-section::before{content:"";width:12px;height:1px;background:var(--rule);margin-right:4px}
  .nav-section::after{content:"";flex:1;height:1px;background:var(--rule);margin-left:6px}
  .nav-link{position:absolute;left:33px;font-size:13.5px;transform:translateY(-50%)}

  .topnav{position:absolute;left:223px;top:31px;display:flex;gap:29px;font-size:11.5px;letter-spacing:.3px}
  .topnav .active{color:var(--red);font-weight:600}
  .btn-logout{position:absolute;left:757px;top:22px;width:112px;height:35px;background:var(--blue);color:var(--white);border-radius:3px;display:flex;align-items:center;justify-content:center;gap:10px;font-weight:700;font-size:11.5px;letter-spacing:.5px}

  .hero{position:absolute;left:196px;top:72px;width:720px;height:476px;border-radius:20px;overflow:hidden;
    background:linear-gradient(180deg,#8f8582 0%,#5f6466 25%,#7e8684 45%,#c8cccd 62%,#8c7a6a 80%,#6e4a33 100%)}
  .hero-title{position:absolute;top:150px;left:0;right:0;text-align:center;color:var(--white);font-weight:700;font-size:38px}
  .hero-sub{position:absolute;top:205px;left:0;right:0;text-align:center;color:var(--white);font-size:13.5px}
  .hero-actions{position:absolute;left:202px;top:164px;margin-top:0;top:164px}
  .hero-actions{top:164px}
  .cta-group{position:absolute;left:202px;top:164px;width:318px;height:36px;display:flex}
  .cta{flex:1;display:flex;align-items:center;justify-content:center;color:var(--white);font-weight:700;font-size:11.5px;letter-spacing:.5px}
  .cta-account{background:var(--red)}
  .cta-nook{background:var(--yellow)}
  .cta-join{position:absolute;left:153px;top:11px;width:14px;height:14px;border-radius:50%;background:var(--white)}
  .hero-arrow{position:absolute;top:230px}

  .categories-title{position:absolute;left:88px;top:624px;font-size:34px;font-weight:800}
  .categories-text{position:absolute;left:89px;top:668px;width:630px;font-size:13px;line-height:20.5px;color:var(--muted)}
  .btn-learn{position:absolute;left:731px;top:655px;width:106px;height:36px;background:var(--navy);color:var(--white);border-radius:3px;display:flex;align-items:center;justify-content:center;font-weight:700;font-size:11.5px;letter-spacing:.4px}

  .connectors{position:absolute;left:0;top:0}
  .hub{position:absolute;left:405px;top:868px;width:100px;text-align:center}
  .hub .dot{width:44px;height:44px;border-radius:50%;background:var(--navy);margin:0 auto 6px}
  .hub .name{font-weight:700;font-size:15px;color:var(--navy)}

  .category-label{position:absolute;font-weight:700;font-size:19.5px;transform:translateX(-50%)}

  .footer{position:absolute;left:0;top:1153px;width:923px;height:47px;background:var(--black);color:var(--white);font-size:11px;display:flex;align-items:center;justify-content:center}
</style>
</head>
<body>
<div class="page">

  <aside class="sidebar">
    <div class="sidebar-brand"><span class="dot"></span>PathHaven</div>
    <div class="nav-global">
      <svg width="16" height="16" viewBox="0 0 24 24" fill="none" stroke="#fff" stroke-width="1.6"><path d="M3 11l9-8 9 8"/><path d="M5 10v10h5v-6h4v6h5V10"/></svg>
      Global
    </div>
    <div class="nav-section" style="top:146px">Manage</div>
    <div class="nav-link" style="top:185px">Overview</div>
    <div class="nav-link" style="top:219px">Guests</div>
    <div class="nav-link" style="top:255px">Unknown User</div>
    <div class="nav-section" style="top:287px">Analyze</div>
    <div class="nav-link" style="top:324px">Alerts</div>
    <div class="nav-link" style="top:359px">Audit Trail</div>
    <div class="nav-link" style="top:393px">Reports</div>
    <div class="nav-section" style="top:429px">Maintain</div>
    <div class="nav-link" style="top:472px">Laseic</div>
    <div class="nav-link" style="top:504px">Organization</div>
  </aside>

  <nav class="topnav">
    <span class="active">HOME</span><span>ABOUT</span><span>CATEGORIES</span><span>BLOGS</span>
  </nav>
  <div class="btn-logout">
    <svg width="14" height="14" viewBox="0 0 24 24" fill="none" stroke="#fff" stroke-width="1.8"><path d="M14 3H5v18h9"/><path d="M10 12h11M17 8l4 4-4 4"/></svg>
    LOGOUT
  </div>

  <section class="hero" role="img" aria-label="Woman sitting on a wooden deck overlooking misty mountain forest">
    <h1 class="hero-title">PathHaven</h1>
    <p class="hero-sub">Accusamus etiusto odiodignis simos ducimus</p>
    <div class="cta-group">
      <div class="cta cta-account">MANAGED ACCOUNT</div>
      <div class="cta cta-nook">QUILLS NOOK</div>
      <span class="cta-join"></span>
    </div>
    <svg class="hero-arrow" style="left:28px" width="12" height="16" viewBox="0 0 12 16" fill="none" stroke="#111" stroke-width="2"><path d="M9 2L3 8l6 6"/></svg>
    <svg class="hero-arrow" style="left:682px" width="12" height="16" viewBox="0 0 12 16" fill="none" stroke="#111" stroke-width="2"><path d="M3 2l6 6-6 6"/></svg>
  </section>

  <h2 class="categories-title">Our Categories</h2>
  <p class="categories-text">Kaerspiciatis unde omnis iste nastus error sit voluptatem accusase sntium doloremque laudantium, totam resm aperiam, eaque ipsa quae seab isello inventore veritatis et quasi.</p>
  <div class="btn-learn">LEARN MORE</div>

  <svg class="connectors" width="923" height="1150" viewBox="0 0 923 1150" fill="none">
    <g stroke="#222" stroke-width="1" stroke-dasharray="4 3">
      <path d="M207 752H354L405 865"/>
      <path d="M706 752H559L509 865"/>
      <path d="M325 1004H370L409 952"/>
      <path d="M588 1004H541L501 952"/>
    </g>
    <!-- Self -->
    <circle cx="166" cy="755" r="25" fill="var(--red)"/>
    <path d="M166 721a34 34 0 1 1-32 44" stroke="var(--red)" stroke-width="1.3"/>
    <g stroke="#fff" stroke-width="1.3"><circle cx="166" cy="746" r="5"/><path d="M157 766v-6a9 9 0 0 1 18 0v6z"/></g>
    <!-- Relationships -->
    <circle cx="746" cy="755" r="25" fill="var(--blue)"/>
    <path d="M776 737a34 34 0 1 0-17 51" stroke="var(--blue)" stroke-width="1.3"/>
    <g stroke="#fff" stroke-width="1.3"><path d="M733 750l7-5 6 3 6-3 7 5M738 756l6 5 4-2 6-4"/></g>
    <!-- Career -->
    <circle cx="285" cy="1003" r="25" fill="var(--yellow)"/>
    <path d="M258 986a34 34 0 0 1 54 0 34 34 0 0 1-17 48" stroke="var(--yellow)" stroke-width="1.3"/>
    <g stroke="#fff" stroke-width="1.3"><circle cx="283" cy="991" r="3"/><path d="M283 995v9l-4 8M283 1004l5 4M275 1014h20M292 1014v-10"/></g>
    <!-- Finance -->
    <circle cx="628" cy="1003" r="25" fill="var(--green)"/>
    <path d="M620 970a34 34 0 1 0 41 27" stroke="var(--green)" stroke-width="1.3"/>
    <g stroke="#fff" stroke-width="1.3"><path d="M618 1013v-10h5v10M625 1013v-15h5v15M632 1013v-20h5v20M614 1015h26"/></g>
  </svg>

  <div class="hub"><div class="dot"></div><div class="name">PathHaven</div></div>

  <div class="category-label" style="left:162px;top:800px">Self</div>
  <div class="category-label" style="left:743px;top:801px">Relationships</div>
  <div class="category-label" style="left:287px;top:1049px">Career</div>
  <div class="category-label" style="left:626px;top:1049px">Finance</div>

  <footer class="footer">©2024. All rights reserved.</footer>
</div>
</body>
</html>
```